Word template for proposals we send to clients

We want a word template designed based on the look/feel of our website. The website is www.brovanex.com.au and while we have pictures of 2 staff on the website we have pictures of other staff if required

the template will be used to send out proposals to potential clients, therefore it has to be professional, modern and compelling for someone to open

Target Market(s)

B2B

Industry/Entity Type

It Company

Font styles to use
Serif

Colors

Designer to choose colors to be used in the design.

Requirements
Must have
• Same look and feel as website
Nice to have
• Dont know what I am missing so anythign you feel i need to add

```html
<!DOCTYPE html>
<html lang="en">
<head>
<meta charset="utf-8">
<title>Brovanex Proposal Template</title>
<link href="https://fonts.googleapis.com/css2?family=Arimo:wght@400;700&family=Montserrat:wght@300;700&display=swap" rel="stylesheet">
<style>
  :root{
    --backdrop:#c8c8cd;
    --paper:#ffffff;
    --lime:#b2c214;
    --leaf:#5b9634;
    --diamond:#a6c21c;
    --slate:#2f3b46;
    --slate-deep:#27313a;
    --brand-green:#3f9a2e;
    --ink:#2b2b2b;
    --muted:#4a4d52;
    --rule:#c9cbcf;
    --photo-a:#8e8aa6;
    --photo-b:#a9bcc4;
  }
  *{margin:0;padding:0;box-sizing:border-box}
  html,body{width:1200px;height:900px;overflow:hidden;background:var(--backdrop)}
  .canvas{position:relative;width:1200px;height:900px}
  .cover{position:absolute;left:80px;top:122px;width:502px;height:652px;display:block}
  .cover-title{font-family:"Montserrat",sans-serif;font-weight:300;font-size:40px;fill:#fff;letter-spacing:1px}
  .cover-brand{font-family:"Montserrat",sans-serif;font-weight:700;font-size:30px;fill:#fff}
  .cover-tagline{font-family:"Montserrat",sans-serif;font-weight:300;font-size:12.5px;fill:#fff;letter-spacing:1.2px}

  .letter{position:absolute;left:629px;top:121px;width:502px;height:651px;background:var(--paper);font-family:"Arimo",sans-serif;color:var(--ink)}
  .letterhead{position:absolute;left:43px;top:36px;display:flex;align-items:center;gap:10px}
  .brand-mark{width:30px;height:30px;background:var(--brand-green)}
  .brand-name{font-family:"Montserrat",sans-serif;font-weight:700;font-size:17px;color:var(--brand-green);line-height:1}
  .brand-tag{font-family:"Montserrat",sans-serif;font-weight:700;font-size:6.5px;color:var(--ink);letter-spacing:.6px;margin-top:3px}
  .contact{position:absolute;right:41px;top:52px;text-align:right;font-size:6px;line-height:8.2px;color:var(--ink);font-style:normal}
  .contact .sep{color:var(--brand-green)}
  .head-rule{position:absolute;left:43px;right:41px;top:92px;height:1px;background:var(--rule)}
  .recipient{position:absolute;left:43px;top:164px;font-size:7.2px;line-height:9px;color:var(--muted)}
  .recipient strong{color:var(--ink)}
  .body{position:absolute;left:43px;top:253px;width:418px;font-size:7.2px;line-height:9px;color:var(--muted)}
  .body p{margin-bottom:8.5px}
  .closing{position:absolute;left:43px;top:480px;font-size:7.2px;line-height:9px;color:var(--muted)}
  .signature-area{position:absolute;left:43px;top:496px;width:84px;height:34px;background:#f1f1f1}
  .signoff{position:absolute;left:43px;top:543px;font-size:7.2px;line-height:9px;color:var(--muted)}
  .signoff strong{color:var(--ink)}
</style>
</head>
<body>
<main class="canvas">

  <svg class="cover" viewBox="0 0 502 652" aria-label="Business proposal cover">
    <defs>
      <clipPath id="page"><rect width="502" height="652"/></clipPath>
    </defs>
    <g clip-path="url(#page)">
      <rect class="cover-base" width="502" height="652" fill="var(--lime)"/>
      <path class="cover-leaf-band" d="M0 0 H144 L502 330 V430 H0 Z" fill="var(--leaf)"/>
      <path class="cover-corner" d="M0 60 C40 62 70 80 92 106 L0 200 Z" fill="var(--slate-deep)"/>
      <rect class="cover-diamond" x="60" y="120" width="260" height="260" rx="44" transform="rotate(45 190 250)" fill="var(--diamond)"/>
      <path class="cover-slate" d="M0 490 C60 470 120 482 178 430 L300 330 C330 306 362 300 402 318 L502 330 V652 H0 Z" fill="var(--slate)"/>
      <path class="cover-slate-wave" d="M0 500 C70 476 130 490 190 446 L300 352 C330 330 370 330 410 345 L502 352 V372 L410 365 C370 352 332 356 304 378 L196 466 C136 510 70 496 0 520 Z" fill="var(--slate-deep)" opacity=".55"/>

      <rect class="staff-photo" role="img" aria-label="Photo of a support consultant with a headset and laptop"
            x="16" y="126" width="282" height="334" rx="18"
            fill="var(--photo-a)" stroke="#fff" stroke-width="5"/>
      <rect class="staff-photo" role="img" aria-label="Photo of a consultant holding a server software guide"
            x="310" y="262" width="200" height="400" rx="18"
            fill="var(--photo-b)" stroke="#fff" stroke-width="5"/>

      <g class="cover-heading" transform="translate(298 14) rotate(45)">
        <text class="cover-title" x="0" y="32">BUSINESS</text>
        <text class="cover-title" x="0" y="78">PROPOSAL</text>
      </g>

      <text class="cover-brand" x="66" y="590">Brovanex</text>
      <text class="cover-tagline" x="66" y="612">CONSULTING  SERVICES</text>
    </g>
  </svg>

  <article class="letter">
    <header class="letterhead">
      <span class="brand-mark"></span>
      <div>
        <div class="brand-name">Brovanex</div>
        <div class="brand-tag">CONSULTING  SERVICES</div>
      </div>
    </header>
    <address class="contact">
      LVL 9/212 KESTREL ST, MELBOURNE, VIC, 3000, AUSTRALIA<br>
      1300 44 71 62 <span class="sep">/</span> INFO@BROVANEX.COM.AU<br>
      WWW.BROVANEX.COM.AU
    </address>
    <div class="head-rule"></div>

    <div class="recipient">
      <strong>Mr. Lucien Harwell</strong><br>
      President and CEO<br>
      Corvalta Labs LLC.<br>
      880 Marlow Avenue, Suite 210<br>
      Eastport, NY 10099
    </div>

    <div class="body">
      <p>Dear Mr. Harwell,</p>
      <p>as Chairperson of the Corporate Conscience Campaign - Helping the Homeless in New York, I am writing this to thank you personally for your company's support in last month's fund-raising effort.</p>
      <p>As I indicated when we spoke on the phone two weeks ago, the campaign was considered a resounding success, raising a total of $1.65 million to-date, significantly exceeding our target of $1 million. Some donations are still trickling in, so we could end up close to a total of $2 million.</p>
      <p>Corvalta Labs was an influential leader throughout the entire three-month campaign. In fact, we couldn't have succeeded without the generous support of your company, both financially, and through your organizational and administrative assistance. Your Team Leader, Mira Olsted was particularly impressive, going above and beyond what we could have expected of someone performing as a volunteer while continuing on with her day-to-day duties. Please convey my special thanks to Mira.</p>
      <p>I would also ask you to convey my sincere thanks and congratulations to all of those other people in your company who contributed in any way to the Helping the Homeless Campaign. Please tell them that the sum of their contributions resulted in a major success that they should all be proud of taking part in.</p>
      <p>I believe that the 27 companies that participated in this effort have set a new standard for social responsibility in this community, and have set a powerful example that will inspire companies and organizations to do the same.</p>
      <p>I look forward to seeing you at the Mayor's special thank you reception next month.</p>
    </div>

    <div class="closing">Yours sincerely,</div>
    <div class="signature-area" role="img" aria-label="Handwritten signature"></div>
    <div class="signoff">
      <strong>Dorian Pelko</strong><br>
      Fundraising Chair
    </div>
  </article>

</main>
</body>
</html>
```